Commercial snow and summer maintenance marketing folders

I'M looking to design a marketing folder for my snow and summer maintenance company.
The folder is a 12''x9'' , i want to fill up the front and back.
Acquire them for the first,keep them for all time is the slogan that will go somewhere in the front ,
I will attach logo, im thinking to having that in the front,top,middle. having a small logo in back bottom middle of page with phone number 647-319-5520,www.brindlegrounds.com . Proud members of Greenway Guild, Wise With Grit And TCPA with small logos beside them. Small writing underneath "2016 Brindle Grounds Ltd. Independently owned and operated. Propriety and Confidential
B2B, Industrial, commercial and municipal customers
Snow Removal

```html
<!DOCTYPE html>
<html lang="en">
<head>
<meta charset="UTF-8">
<title>Brindle Grounds – Marketing Folder</title>
<link rel="stylesheet" href="https://fonts.googleapis.com/css2?family=Open+Sans:wght@400;600;700&display=swap">
<style>
  :root {
    --green-deep: #4e9a1c;
    --green-mid: #86c83a;
    --green-light: #c9ea6a;
    --green-text: #8cc63f;
    --ink: #4a5350;
    --ink-dark: #3b4442;
    --paper: #ffffff;
    --badge-grey: #c9cdcc;
    --badge-blue: #9cc6e6;
  }
  * { margin: 0; padding: 0; box-sizing: border-box; }
  html, body {
    width: 1200px; height: 800px; overflow: hidden;
    background: var(--paper);
    font-family: "Open Sans", Arial, sans-serif;
  }
  .folder {
    position: relative; width: 1200px; height: 800px;
    display: flex;
  }
  .panel { position: relative; width: 600px; height: 800px; overflow: hidden; background: var(--paper); }

  /* Back panel */
  .back-glow {
    position: absolute; left: 0; top: 0; width: 600px; height: 420px;
    background: linear-gradient(180deg, var(--green-deep) 0%, var(--green-mid) 35%, var(--green-light) 62%, rgba(255,255,255,0) 100%);
  }
  .back-brand {
    position: absolute; left: 0; top: 590px; width: 600px;
    display: flex; justify-content: center; align-items: center; gap: 10px;
  }
  .back-brand .dot { width: 14px; height: 14px; border-radius: 50%; background: var(--green-mid); }
  .back-brand .name {
    font-weight: 700; font-size: 24px; letter-spacing: 3px;
    color: var(--ink); text-transform: uppercase;
  }
  .contact {
    position: absolute; left: 0; top: 671px; width: 600px;
    text-align: center; font-weight: 700; font-size: 14px; color: var(--ink-dark);
  }
  .contact .sep { color: var(--green-text); margin: 0 6px; }
  .members {
    position: absolute; left: 0; top: 700px; width: 600px;
    display: flex; justify-content: center; align-items: center; gap: 12px;
  }
  .members .label {
    font-size: 7px; font-weight: 600; line-height: 1.1; color: var(--ink); text-align: right;
  }
  .members .divider { width: 2px; height: 40px; background: var(--green-text); }
  .badge { height: 26px; border-radius: 3px; background: var(--badge-grey); }
  .badge.guild { width: 118px; }
  .badge.grit { width: 82px; background: var(--badge-blue); }
  .badge.assoc { width: 80px; }
  .legal {
    position: absolute; left: 0; top: 752px; width: 600px;
    text-align: center; font-size: 9.5px; color: var(--green-text);
  }

  /* Front panel */
  .front-brand {
    position: absolute; left: 600px; top: 0; width: 600px; height: 380px;
    display: flex; justify-content: center; align-items: center; gap: 16px;
  }
  .front-brand .dot { width: 30px; height: 30px; border-radius: 50%; background: var(--green-mid); }
  .front-brand .name {
    font-weight: 700; font-size: 52px; letter-spacing: 7px;
    color: var(--ink); text-transform: uppercase;
  }
  .front-glow {
    position: absolute; left: 0; top: 400px; width: 600px; height: 400px;
    background: linear-gradient(180deg, rgba(255,255,255,0) 0%, var(--green-light) 30%, var(--green-mid) 60%, var(--green-deep) 100%);
  }
  .slogan {
    position: absolute; left: 0; top: 430px; width: 600px;
    text-align: center; font-weight: 700; font-size: 20px; line-height: 34px;
    color: var(--ink); font-variant: small-caps; letter-spacing: 0.5px;
  }
</style>
</head>
<body>
  <div class="folder">
    <section class="panel back">
      <div class="back-glow" role="img" aria-label="Soft green bokeh light background fading to white"></div>
      <div class="back-brand">
        <span class="dot"></span>
        <span class="name">Brindle Grounds</span>
      </div>
      <p class="contact">T: 647-319-5520<span class="sep">I</span>www.brindlegrounds.com</p>
      <div class="members">
        <span class="label">PROUD<br>MEMBERS</span>
        <span class="badge guild" role="img" aria-label="Greenway Guild membership badge"></span>
        <span class="divider"></span>
        <span class="badge grit" role="img" aria-label="Wise With Grit program badge"></span>
        <span class="divider"></span>
        <span class="badge assoc" role="img" aria-label="TCPA association badge"></span>
      </div>
      <p class="legal">2016 Brindle Grounds Ltd. Independently owned and operated. Propriety and Confidential</p>
    </section>

    <section class="panel front">
      <div class="front-glow" role="img" aria-label="Soft green bokeh light background rising from the bottom"></div>
      <div class="front-brand" style="left:0;">
        <span class="dot"></span>
        <span class="name">Brindle Grounds</span>
      </div>
      <p class="slogan">Acquire them for the first,<br>keep them for all time</p>
    </section>
  </div>
</body>
</html>
```